Web design required

1-We need a web design for existing company based in New Zealand
2-We build residential house and light commercial
3-We has in-house designer which allow us can provide interior design
4-We modeling project before site construction, which enable both client and construction team to visually analysis whole project,

Target Market(s)

middle class residential house market
Ref: http://www.brackwellbuilders.co.nz/

Industry/Entity Type

Construction Company

Number of Pages Required

1 page

Font styles to use
Sans Serif
Other font styles liked:
• Such as : Central Gothic or similar which has more design taste

Colors

Designer to choose colors to be used in the design.

Requirements
Must have
• Front sheet, contact information, sample project

```html
<!DOCTYPE html>
<html lang="en">
<head>
<meta charset="utf-8">
<title>Kestrel Homes</title>
<link rel="stylesheet" href="https://fonts.googleapis.com/css2?family=Open+Sans:wght@400;600;700;800&display=swap">
<style>
:root{
  --blue:#1a6bb3;
  --blue-dark:#155a98;
  --navy:#1d2a38;
  --ink:#2b2f33;
  --muted:#6d7378;
  --light:#ececec;
  --white:#ffffff;
  --field:#f1f1f1;
}
*{box-sizing:border-box;margin:0;padding:0}
html,body{width:1200px;height:2880px;overflow:hidden}
body{font-family:"Open Sans",Arial,sans-serif;color:var(--ink);background:var(--white)}
.page{position:relative;width:1200px;height:2880px}

.topbar{height:112px;display:flex;align-items:center;justify-content:space-between;padding:0 72px}
.brand{display:flex;align-items:center;gap:14px}
.brand-mark{width:34px;height:34px;background:var(--blue)}
.brand-name{font-weight:700;font-size:34px;color:var(--blue);letter-spacing:1px;line-height:1}
.top-actions{display:flex;align-items:center;gap:22px}
.top-phone{display:flex;align-items:center;gap:12px;font-weight:700;font-size:30px;color:var(--navy)}
.btn-quote{background:var(--navy);color:var(--white);font-size:18px;font-weight:600;padding:12px 22px;border-radius:4px}

.nav{height:56px;background:var(--blue);display:flex;align-items:center;padding:0 100px;gap:46px;color:var(--white);font-size:15px;font-weight:600;text-transform:uppercase}
.nav .search{margin-left:auto;width:300px;border-bottom:1px solid rgba(255,255,255,.6);font-weight:400;text-transform:none;padding-bottom:4px;display:flex;justify-content:space-between;color:rgba(255,255,255,.85)}

.hero{position:relative;height:504px;background:linear-gradient(180deg,#7f98ad 0%,#a9b8c3 45%,#d6d9d6 70%,#6f7f5e 100%);color:var(--white);text-align:center}
.hero-shade{position:absolute;inset:0;background:rgba(20,40,60,.28)}
.hero-title{position:relative;padding-top:130px;font-size:64px;font-weight:800;letter-spacing:1px}
.hero-copy{position:relative;width:760px;margin:14px auto 0;font-size:17px;line-height:1.5}
.hero-play{position:absolute;left:564px;top:312px;width:72px;height:72px;border-radius:50%;background:rgba(26,107,179,.85)}

.services{height:376px;display:flex;gap:28px;padding:64px 72px 0}
.service{position:relative;flex:1;height:268px;background:linear-gradient(180deg,#4f7fa9,#2e5f8d);color:var(--white);display:flex;flex-direction:column;align-items:center;justify-content:center;gap:18px}
.service::after{content:"";position:absolute;inset:0;background:rgba(26,107,179,.35)}
.service-title{position:relative;z-index:1;font-size:34px;font-weight:700;text-transform:uppercase}
.service svg{position:relative;z-index:1}

.about{height:452px;background:var(--light);display:flex;gap:40px;padding:72px 80px 0}
.about-photo{width:432px;height:360px;background:linear-gradient(135deg,#c9a46a,#8aa4c0 55%,#4d6e90)}
.about-text{flex:1;padding-top:6px}
.eyebrow{font-size:18px;color:var(--blue);text-transform:uppercase;letter-spacing:1px}
.about-title{font-size:44px;font-weight:800;color:var(--blue);text-transform:uppercase;margin:4px 0 16px}
.about-copy{font-size:16px;line-height:1.6;color:var(--muted)}
.btn-dark{display:inline-block;margin-top:24px;background:var(--navy);color:var(--white);font-size:18px;font-weight:600;padding:12px 30px;border-radius:4px;text-transform:uppercase}

.projects{height:560px;margin-top:20px;background:var(--blue);color:var(--white);text-align:center;padding-top:60px}
.projects .eyebrow{color:rgba(255,255,255,.85);font-size:16px}
.projects-title{font-size:48px;font-weight:700;text-transform:uppercase;margin-top:2px}
.gallery{display:flex;margin-top:38px;height:280px}
.gallery-item{flex:1;position:relative}
.g1{background:linear-gradient(135deg,#e9e9e9,#7b7f84 60%,#2c2f33)}
.g2{background:linear-gradient(180deg,#9fc0de,#d0d8d8 55%,#7f9466);outline:6px solid var(--white);outline-offset:-6px}
.g2::before{content:"";position:absolute;inset:6px;background:rgba(26,107,179,.45)}
.g2 svg{position:absolute;left:50%;top:50%;transform:translate(-50%,-50%)}
.g3{background:linear-gradient(135deg,#f2e2c4,#b08756 50%,#5d4a38)}
.g4{background:linear-gradient(180deg,#8db3d8,#e5e5e0 55%,#7a925d)}
.projects-foot{display:flex;justify-content:space-between;align-items:center;padding:30px 80px 0;font-size:18px;font-weight:700;text-transform:uppercase}
.arrows{display:flex;gap:22px}

.lower{height:520px;display:flex;gap:90px;padding:40px 80px 0}
.contact,.news{flex:1}
.lower .eyebrow{font-size:16px}
.section-title{font-size:44px;font-weight:700;color:var(--blue);text-transform:uppercase;margin:2px 0 18px}
.field{background:var(--field);height:44px;margin-bottom:12px;padding:11px 14px;font-size:14px;color:#9a9fa3;width:470px}
.field.message{height:84px}
.btn-submit{display:inline-block;background:var(--navy);color:var(--white);font-size:16px;font-weight:600;padding:12px 24px;border-radius:3px;text-transform:uppercase;margin-top:6px}
.news-item{display:flex;gap:22px;margin-bottom:30px}
.news-thumb{width:150px;height:118px;flex:none}
.nt1{background:linear-gradient(135deg,#d9b98a,#8b6a48)}
.nt2{background:linear-gradient(180deg,#a7bfd6,#d9d9d2 60%,#7e8f6a)}
.news-date{display:flex;align-items:center;gap:8px;color:var(--blue);font-weight:700;font-size:16px}
.news-head{font-size:20px;font-weight:700;line-height:1.3;margin:6px 0 4px;color:var(--ink)}
.news-copy{font-size:15px;color:var(--muted);line-height:1.45}

.contact-band{height:120px;background:var(--blue);color:var(--white);display:flex;align-items:center;padding:0 80px;font-size:22px}
.contact-band .item{display:flex;align-items:center;gap:18px;margin-right:160px}
.icon-ring{width:46px;height:46px;border-radius:50%;background:rgba(255,255,255,.2);display:flex;align-items:center;justify-content:center}
.socials{margin-left:auto;display:flex;gap:14px}
.socials span{width:48px;height:48px;border-radius:50%;border:2px solid var(--white)}

.footer{height:140px;display:flex;justify-content:space-between;align-items:center;padding:0 80px}
.footer-links{font-size:16px;color:var(--muted)}
.footer-links span{margin:0 8px}
.copyright{font-size:13px;color:var(--muted);margin-top:10px}
.footer .brand-name{font-size:30px}
.footer .brand-mark{width:30px;height:30px}
</style>
</head>
<body>
<div class="page">

  <header class="topbar">
    <div class="brand"><span class="brand-mark"></span><span class="brand-name">KESTREL HOMES</span></div>
    <div class="top-actions">
      <div class="top-phone">
        <svg width="30" height="30" viewBox="0 0 24 24"><path fill="#1d2a38" d="M6.6 10.8a15 15 0 0 0 6.6 6.6l2.2-2.2c.3-.3.7-.4 1-.2 1.1.4 2.3.6 3.6.6.6 0 1 .4 1 1V20c0 .6-.4 1-1 1A17 17 0 0 1 3 4c0-.6.4-1 1-1h3.5c.6 0 1 .4 1 1 0 1.3.2 2.5.6 3.6.1.3 0 .7-.2 1z"/></svg>
        021 555 0147
      </div>
      <div class="btn-quote">REQUEST A QUOTE</div>
    </div>
  </header>

  <nav class="nav">
    <span>Home ▾</span><span>About</span><span>Services</span><span>Projects</span><span>News</span><span>Contact</span>
    <span class="search"><span>Search…</span><span>⌕</span></span>
  </nav>

  <section class="hero" role="img" aria-label="Photo of a modern two-storey white house with a landscaped front garden">
    <div class="hero-shade"></div>
    <h1 class="hero-title">WE BUILD YOUR DREAMS....</h1>
    <p class="hero-copy">We design, model and build quality homes and light commercial spaces across New Zealand, with in-house interior design from concept to handover.</p>
    <svg class="hero-play" viewBox="0 0 72 72"><circle cx="36" cy="36" r="36" fill="#1a6bb3" opacity=".85"/><path d="M29 23l20 13-20 13z" fill="#fff"/></svg>
  </section>

  <section class="services">
    <div class="service" role="img" aria-label="Photo of a finished residential house">
      <div class="service-title">Residential House</div>
      <svg width="40" height="16" viewBox="0 0 40 16"><path d="M2 8h34M28 2l8 6-8 6" stroke="#fff" stroke-width="2.5" fill="none"/></svg>
    </div>
    <div class="service" role="img" aria-label="Photo of a light commercial building">
      <div class="service-title">Light Commercial</div>
      <svg width="40" height="16" viewBox="0 0 40 16"><path d="M2 8h34M28 2l8 6-8 6" stroke="#fff" stroke-width="2.5" fill="none"/></svg>
    </div>
  </section>

  <section class="about">
    <div class="about-photo" role="img" aria-label="Photo of a builder reviewing house plans with a couple"></div>
    <div class="about-text">
      <div class="eyebrow">Welcome to</div>
      <h2 class="about-title">Kestrel Homes</h2>
      <p class="about-copy">Lorem ipsum is simply dummy text of the printing and typesetting industry. Lorem ipsum has been the industry's standard dummy text ever since the 1500s, when an unknown printer took a galley of type and scrambled it to make a type specimen book. It has survived not only five centuries, but also the leap into electronic typesetting, remaining essentially unchanged.</p>
      <span class="btn-dark">Read more</span>
    </div>
  </section>

  <section class="projects">
    <div class="eyebrow">What we do</div>
    <h2 class="projects-title">Our Projects</h2>
    <div class="gallery">
      <div class="gallery-item g1" role="img" aria-label="Photo of a modern interior with kitchen and living area"></div>
      <div class="gallery-item g2" role="img" aria-label="Photo of a contemporary house exterior">
        <svg width="64" height="64" viewBox="0 0 64 64"><circle cx="27" cy="27" r="17" stroke="#fff" stroke-width="4" fill="none"/><path d="M40 40l16 16M27 19v16M19 27h16" stroke="#fff" stroke-width="4"/></svg>
      </div>
      <div class="gallery-item g3" role="img" aria-label="Photo of builders inside a timber frame under construction"></div>
      <div class="gallery-item g4" role="img" aria-label="Photo of a modern family home with a lawn"></div>
    </div>
    <div class="projects-foot">
      <span>View all projects ⟶</span>
      <span class="arrows"><span>‹</span><span>›</span></span>
    </div>
  </section>

  <section class="lower">
    <div class="contact">
      <div class="eyebrow">Contact us</div>
      <h2 class="section-title">Get in touch</h2>
      <div class="field">Name*</div>
      <div class="field">Email*</div>
      <div class="field">Phone*</div>
      <div class="field message">Message*</div>
      <span class="btn-submit">Submit</span>
    </div>
    <div class="news">
      <div class="eyebrow">Recent post</div>
      <h2 class="section-title">Latest News</h2>
      <div class="news-item">
        <div class="news-thumb nt1" role="img" aria-label="Photo of a builder on a construction site"></div>
        <div>
          <div class="news-date">▣ 06 Nov 2017</div>
          <div class="news-head">Lorem ipsum is the simply dummy text of the printing and ?</div>
          <p class="news-copy">Lorem ipsum is simply dummy text of the printing and typesetting industry.</p>
        </div>
      </div>
      <div class="news-item">
        <div class="news-thumb nt2" role="img" aria-label="Photo of a newly built house"></div>
        <div>
          <div class="news-date">▣ 06 Nov 2017</div>
          <div class="news-head">Lorem ipsum is the simply dummy text of the printing and ?</div>
          <p class="news-copy">Lorem ipsum is simply dummy text of the printing and typesetting industry.</p>
        </div>
      </div>
    </div>
  </section>

  <section class="contact-band">
    <div class="item">
      <span class="icon-ring"><svg width="22" height="22" viewBox="0 0 24 24"><path fill="#fff" d="M6.6 10.8a15 15 0 0 0 6.6 6.6l2.2-2.2c.3-.3.7-.4 1-.2 1.1.4 2.3.6 3.6.6.6 0 1 .4 1 1V20c0 .6-.4 1-1 1A17 17 0 0 1 3 4c0-.6.4-1 1-1h3.5c.6 0 1 .4 1 1 0 1.3.2 2.5.6 3.6.1.3 0 .7-.2 1z"/></svg></span>
      021 555 0147
    </div>
    <div class="item">
      <span class="icon-ring"><svg width="22" height="18" viewBox="0 0 22 18"><rect x="1" y="1" width="20" height="16" fill="none" stroke="#fff" stroke-width="2"/><path d="M1 2l10 8 10-8" fill="none" stroke="#fff" stroke-width="2"/></svg></span>
      info@kestrelhomes.co.nz
    </div>
    <div class="socials"><span></span><span></span><span></span></div>
  </section>

  <footer class="footer">
    <div>
      <div class="footer-links">Home<span>|</span>About<span>|</span>Services<span>|</span>Projects<span>|</span>News<span>|</span>Contact</div>
      <div class="copyright">© KESTREL HOMES · 2017. All Rights Reserved</div>
    </div>
    <div class="brand"><span class="brand-mark"></span><span class="brand-name">KESTREL HOMES</span></div>
  </footer>

</div>
</body>
</html>
```